Create a Shopify weblayout for Haverlow Fashion Boutique

I would like a new website layout for my online fashion boutique www.haverlow-shop.example. My new online boutique is inspired by the 2 English writers of the 19th century. These books come from old English literature. Haverlow is a fictitious place withing these inspiring love stories. My boutique idea is inspired by old English landscape, unprecedented magic and influenced by bonds between improbable characters. My boutique is for woman initially, but I would like to add male products sometime in the future, hence the logo should be gender neutral.

I have started with a logo which I deciding upon these days. However, the professional website layout that I am looking for would be inspired by a creative visual from the above descriptions.

I do like white/black color scheme, but I would also like the layout to incorporate an additional color plus an additional design element. I was thinking of floral inspirations, like roses or green wine leaves, perhaps. I would like something with a mix of modern, magic, and eclectic. Thank you all in advance for your igniting ideas.

Project Deadline Extended Reason: Project extended due to holiday season. We are working on submitting feedback regarding our desired layout. Added Thursday, November 24, 2016

Target Market(s)

Online boutique for women and man clothing.

Industry/Entity Type

Fashion

Coding

Coded - Design and coding required

Number of Pages Required

4 page

Font styles to use
Other font styles liked:
• readable, but elegant and artsy

Requirements
Must have
• Elegant, artsy and legible. Embrace the logo (vector files will be uploaded shortly)
• Files must support use with Shopify. More boutique style less commercial. Simple details are nice. I like the efficiency of the commercial sites. Must have a mobile version. EXAMPLE: http://www.mabelsonwestcedar.example/ THIS IS A BEAUTIFUL SITE. in place of the yellow line it would be nice to have a vine maybe?
• Although i am stern on this, i don't mean this with any disrespect ever but please, don't call me or email me on my personal email. If we need to connect, we can do so after i pick a design. Thank you.
Nice to have
• It would be nice if the tree of the logo would be incorporate somewhere in the website. We are very much interested in little details. Please inspire us.

```html
<!DOCTYPE html>
<html lang="en">
<head>
<meta charset="utf-8">
<title>Haverlow Fashion Boutique</title>
<link rel="stylesheet" href="https://fonts.googleapis.com/css2?family=Oswald:wght@400;500&family=Roboto:wght@300;400;500&display=swap">
<style>
:root{
  --ink:#111111;
  --night:#0b0b0b;
  --paper:#ffffff;
  --coral:#f57b6e;
  --grey-text:#8a8a8a;
  --body-text:#2b2b2b;
  --rule:#e6e6e6;
  --footer-text:#e9e9e9;
}
*{box-sizing:border-box;margin:0;padding:0}
html,body{width:667px;height:1200px;overflow:hidden;background:var(--paper)}
body{font-family:'Roboto',sans-serif;color:var(--body-text)}
.page{position:relative;width:667px;height:1200px;overflow:hidden}
.abs{position:absolute}

/* top bar */
.promo-bar{left:0;top:0;width:667px;height:22px;background:var(--night);color:var(--paper);
  font-family:'Oswald',sans-serif;font-size:9px;letter-spacing:.2px;display:flex;align-items:center;justify-content:center;gap:4px}

/* header */
.search-icon{left:44px;top:57px}
.brand{left:0;top:48px;width:667px;text-align:center;font-family:'Roboto',sans-serif;font-weight:400;font-size:27px;color:var(--ink);letter-spacing:1px}
.cart{left:593px;top:56px}
.cart-count{left:604px;top:50px;width:14px;height:14px;border-radius:50%;background:#e8e8e8;font-size:7px;color:#555;display:flex;align-items:center;justify-content:center}
.header-rule{left:48px;top:86px;width:570px;height:1px;background:var(--rule)}
.main-nav{left:0;top:94px;width:667px;height:12px;font-size:7.5px;color:#333;letter-spacing:.2px}
.main-nav span{position:absolute;transform:translateX(-50%);white-space:nowrap}

/* hero */
.hero{left:0;top:111px;width:667px;height:319px;
  background:radial-gradient(ellipse 90px 150px at 70% 55%,#b49a90 0%,rgba(180,154,144,0) 100%),
  radial-gradient(ellipse 140px 45px at 70% 92%,#a9a7a2 0%,rgba(169,167,162,0) 100%),
  linear-gradient(180deg,#8f9d8e 0%,#5f7459 30%,#3f5a3a 65%,#4d5f48 85%,#6f766c 100%)}
.hero-title{left:60px;top:232px;width:248px;text-align:center;color:var(--paper);font-family:'Oswald',sans-serif;font-weight:500;line-height:1}
.hero-title .line-one{display:block;font-size:26px}
.hero-title .line-two{display:block;font-size:33px;margin-top:2px}
.shop-now{left:146px;top:304px;width:74px;height:21px;background:var(--coral);color:var(--paper);font-size:7px;display:flex;align-items:center;justify-content:center;letter-spacing:.3px}
.slider-dots{left:322px;top:405px;display:flex;gap:3px}
.slider-dots i{width:5px;height:5px;border-radius:50%;background:var(--paper)}
.slider-dots i.active{background:var(--coral)}

/* section titles */
.section-title{left:0;width:667px;text-align:center;font-weight:300;font-size:14.5px;color:var(--ink);letter-spacing:.2px}

/* products */
.product{top:488px;width:140px}
.product-photo{width:140px;height:174px;position:relative}
.product-name{margin-top:11px;font-size:7.5px;color:var(--ink)}
.product-price{margin-top:3px;font-size:7.5px;color:var(--grey-text)}
.wish-flag{position:absolute;right:0;top:0}
.section-rule{left:77px;top:734px;width:513px;height:1px;background:var(--rule)}

/* gallery */
.gallery-tile{top:790px;width:91px;height:88px}
.gallery-tile.active{background:var(--coral);opacity:.92;box-shadow:0 3px 8px rgba(0,0,0,.3);display:flex;align-items:center;justify-content:center;gap:5px}

/* newsletter */
.email-field{left:150px;top:944px;width:299px;height:27px;border:1px solid #e3e3e3;font-size:7px;color:#777;padding-left:12px;display:flex;align-items:center}
.subscribe{left:449px;top:944px;width:74px;height:27px;background:var(--coral);color:var(--paper);font-size:7.5px;font-weight:500;display:flex;align-items:center;justify-content:center}

/* footer */
.treeline{left:0;top:994px;width:667px;height:40px;background:linear-gradient(180deg,rgba(11,11,11,0) 0%,rgba(11,11,11,.6) 45%,var(--night) 100%)}
.footer{left:0;top:1033px;width:667px;height:167px;background:var(--night);color:var(--footer-text)}
.footer-col{top:35px}
.footer-col h4{font-weight:300;font-size:9px;color:var(--paper);margin-bottom:7px;letter-spacing:.2px}
.footer-col li{list-style:none;font-size:6.5px;line-height:13.3px}
.contact{left:512px;top:33px;font-size:6.5px;width:130px}
.contact-row{display:flex;align-items:flex-start;gap:7px;margin-bottom:7px}
.contact-row.phone{font-size:10px;align-items:center}
.socials{display:flex;gap:4px}
.socials i{width:16px;height:16px;border:1px solid #cfcfcf;border-radius:50%;display:flex;align-items:center;justify-content:center}
.socials i::after{content:"";width:4px;height:4px;border-radius:50%;background:#ffffff}
.footer-rule{left:49px;top:141px;width:570px;height:1px;background:#222}
.copyright{left:49px;top:151px;font-size:6.5px}
.legal{right:52px;top:151px;font-size:6.5px}
.to-top{left:634px;top:133px;width:18px;height:18px;background:var(--coral);display:flex;align-items:center;justify-content:center}
</style>
</head>
<body>
<div class="page">

  <div class="abs promo-bar">
    <svg width="8" height="6" viewBox="0 0 8 6"><path d="M0 3h7M5 1l2 2-2 2" stroke="#fff" stroke-width=".8" fill="none"/></svg>
    FREE SHIPPING ON ALL ORDERS OVER $125
  </div>

  <svg class="abs search-icon" width="12" height="12" viewBox="0 0 12 12"><circle cx="5" cy="5" r="3.6" stroke="#111" stroke-width="1.4" fill="none"/><path d="M7.6 7.6L11 11" stroke="#111" stroke-width="1.6"/></svg>
  <div class="abs brand">Haverlow</div>
  <svg class="abs cart" width="13" height="14" viewBox="0 0 13 14"><path d="M1.5 4.5h10l-.8 8.5H2.3z" stroke="#f57b6e" stroke-width="1.2" fill="none"/><path d="M4.2 6V3.4a2.3 2.3 0 0 1 4.6 0V6" stroke="#f57b6e" stroke-width="1.1" fill="none"/></svg>
  <div class="abs cart-count">0</div>
  <div class="abs header-rule"></div>

  <nav class="abs main-nav">
    <span style="left:198px">HOME</span>
    <span style="left:240px">ABOUT</span>
    <span style="left:285px">EVENTS</span>
    <span style="left:330px">SHOP <svg width="5" height="4" viewBox="0 0 5 4"><path d="M.5 1l2 2 2-2" stroke="#333" stroke-width=".8" fill="none"/></svg></span>
    <span style="left:374px">RETURNS</span>
    <span style="left:426px">CONTACT</span>
    <span style="left:471px">SALE</span>
  </nav>

  <div class="abs hero" role="img" aria-label="Woman in a checked shirt sitting on a rock above a misty forest valley, a dark red hat beside her"></div>
  <h1 class="abs hero-title"><span class="line-one">THE ULTIMATE</span><span class="line-two">PERFECT MATCH</span></h1>
  <div class="abs shop-now">SHOP NOW</div>
  <div class="abs slider-dots"><i class="active"></i><i></i></div>

  <h2 class="abs section-title" style="top:462px">WHAT'S NEW?</h2>

  <div class="abs product" style="left:48px">
    <div class="product-photo" style="background:radial-gradient(ellipse 22px 50px at 50% 45%,#f6f1e8 0%,rgba(246,241,232,0) 100%),linear-gradient(180deg,#dcdad9 0%,#d4d2d0 60%,#f0efee 100%)" role="img" aria-label="Model in a white blazer and skirt on a runway"></div>
    <div class="product-name">Boutique haverlow Dress</div>
    <div class="product-price">$ 64.00</div>
  </div>
  <div class="abs product" style="left:192px">
    <div class="product-photo" style="background:radial-gradient(ellipse 30px 55px at 50% 60%,#b9b6c4 0%,rgba(185,182,196,0) 100%),linear-gradient(180deg,#e3e2e2 0%,#d8d6d5 60%,#f0efee 100%)" role="img" aria-label="Model in a pale tulle skirt and mint jacket on a runway"></div>
    <div class="product-name">Boutique haverlow Dress</div>
    <div class="product-price">$ 37.00</div>
  </div>
  <div class="abs product" style="left:335px">
    <div class="product-photo" style="background:radial-gradient(ellipse 20px 25px at 52% 65%,#3a3a3a 0%,rgba(58,58,58,0) 100%),linear-gradient(180deg,#dedcdb 0%,#d6d4d2 60%,#f0efee 100%)" role="img" aria-label="Model in a white top and black skirt on a runway">
      <svg class="wish-flag" width="27" height="27" viewBox="0 0 27 27"><path d="M0 0h27v27z" fill="#f57b6e"/><path d="M21 9.5c-.9-1.5-2.7-.8-2.7.5 0-1.3-1.8-2-2.7-.5-.8 1.4 1.2 3 2.7 4 1.5-1 3.5-2.6 2.7-4z" fill="#fff" stroke="#333" stroke-width=".5" transform="translate(-2 -4)"/></svg>
    </div>
    <div class="product-name">Boutique haverlow Dress</div>
    <div class="product-price">$ 72.00</div>
  </div>
  <div class="abs product" style="left:478px">
    <div class="product-photo" style="background:radial-gradient(ellipse 28px 50px at 50% 55%,#f0552f 0%,rgba(240,85,47,0) 100%),linear-gradient(180deg,#e3e1e0 0%,#d9d7d6 60%,#f0efee 100%)" role="img" aria-label="Model in an orange dress on a runway"></div>
    <div class="product-name">Boutique haverlow Dress</div>
    <div class="product-price">$ 50.00</div>
  </div>

  <div class="abs section-rule"></div>

  <h2 class="abs section-title" style="top:760px">TAG US ON SNAPLINE HAVERLOW</h2>

  <div class="abs gallery-tile" style="left:1px;background:linear-gradient(160deg,#eef0f3,#b8a6c6)" role="img" aria-label="Man in a lilac shirt"></div>
  <div class="abs gallery-tile" style="left:97px;background:linear-gradient(160deg,#7c6a8e,#5a79b6)" role="img" aria-label="Couple in blue and purple shirts"></div>
  <div class="abs gallery-tile active" style="left:191px" role="img" aria-label="Woman in a light dress outdoors">
    <svg width="9" height="8" viewBox="0 0 9 8"><path d="M4.5 7.3C2 5.6.5 4.3.5 2.7.5 1.5 1.4.6 2.5.6c.8 0 1.5.5 2 1.1.5-.6 1.2-1.1 2-1.1 1.1 0 2 .9 2 2.1 0 1.6-1.5 2.9-4 4.6z" stroke="#fff" stroke-width=".8" fill="none"/></svg>
    <svg width="9" height="8" viewBox="0 0 9 8"><path d="M.6.6h7.8v5H3.2L1.4 7.2V5.6H.6z" stroke="#fff" stroke-width=".8" fill="none"/></svg>
  </div>
  <div class="abs gallery-tile" style="left:287px;background:linear-gradient(160deg,#5a4030,#c9b49b)" role="img" aria-label="Man in a white tee by a wooden wall"></div>
  <div class="abs gallery-tile" style="left:383px;background:linear-gradient(160deg,#cfcac2,#8a8479)" role="img" aria-label="Woman in a white dress in sunlight"></div>
  <div class="abs gallery-tile" style="left:479px;background:linear-gradient(160deg,#3a342e,#8d7760)" role="img" aria-label="Man in a beige jacket"></div>
  <div class="abs gallery-tile" style="left:576px;background:linear-gradient(160deg,#253a5c,#c9cfd8)" role="img" aria-label="Woman in a blue top and white skirt"></div>

  <h2 class="abs section-title" style="top:917px">JOIN OUR EMAIL LIST</h2>
  <div class="abs email-field">Your Email</div>
  <div class="abs subscribe">SUBSCRIBE</div>

  <div class="abs treeline" role="img" aria-label="Silhouette of a pine forest along the top of the footer"></div>

  <footer class="abs footer">
    <div class="abs footer-col" style="left:49px">
      <h4>INFORMATION</h4>
      <ul><li>About Us</li><li>Customer Service</li><li>Privacy Policy</li><li>Site Map</li><li>Orders and Returns</li><li>Contact Us</li></ul>
    </div>
    <div class="abs footer-col" style="left:197px">
      <h4>WHY BUY FROM US</h4>
      <ul><li>Shipping &amp; Returns</li><li>Secure Shopping</li><li>International Shipping</li><li>Affiliates</li><li>Group Sales</li></ul>
    </div>
    <div class="abs footer-col" style="left:370px">
      <h4>MY ACCOUNT</h4>
      <ul><li>Sign In</li><li>View Cart</li><li>My Wishlist</li><li>Track My Order</li><li>Help</li></ul>
    </div>
    <div class="abs contact">
      <div class="contact-row">
        <svg width="10" height="9" viewBox="0 0 10 9"><path d="M5 .5L.5 4.3h1.3V8.5h2.4V6h1.6v2.5h2.4V4.3h1.3z" fill="#fff"/></svg>
        <span>00200 St. Haverlow Place,<br>Street 458</span>
      </div>
      <div class="contact-row phone">
        <svg width="9" height="9" viewBox="0 0 9 9"><path d="M1.8.5l1.6 2-1 1.1c.5 1.2 1.5 2.2 2.9 2.9l1.1-1 2 1.6-.9 1.4C4.6 8.4.6 4.4.5 1.4z" fill="#fff"/></svg>
        <span>+41 ( 372 ) 915</span>
      </div>
      <div class="contact-row">
        <svg width="10" height="7" viewBox="0 0 10 7"><rect x=".5" y=".5" width="9" height="6" fill="#fff"/><path d="M.5.5L5 4 9.5.5" stroke="#0b0b0b" stroke-width=".8" fill="none"/></svg>
        <span>info@haverlow-shop.example</span>
      </div>
      <div class="socials"><i></i><i></i><i></i><i></i></div>
    </div>
    <div class="abs footer-rule"></div>
    <div class="abs copyright">Copyright 2016 | All Right Reserved</div>
    <div class="abs legal">Terms &amp; Conditions &nbsp;|&nbsp; Privacy Policy</div>
    <div class="abs to-top"><svg width="6" height="4" viewBox="0 0 6 4"><path d="M.5 3.5L3 1l2.5 2.5" stroke="#fff" stroke-width=".9" fill="none"/></svg></div>
  </footer>

</div>
</body>
</html>
```